NEW Modern Sleek Business Card for VR Language Startup

Our startup is using VR to lead the next wave of world language education. We need a two-sided business card that introduces the larger organization (Quorvel Language Inc) and our contact info on one side and shows the product, Lumidrasca, on the other side.

Side 1 (contact info)= Quorvel Logo and Contact info (name, title, phone, email)

Side 2 (product)= Lumidrasc logo, text, and website
Text= Culturally Immersive Language Learning Games
Website= www.lumidrasc.example

Target Market(s)

Education, Technology

Contact Information for Business Card

Contact info will be updated upon approval of the design. For now, put this as a placeholder.

Perry Hollins
Founder & CEO
phollins@mailtrove.example
(555)-014-2736

Font styles to use
Other font styles liked:
• Gibson and Century Gothic are the brand fonts

Requirements
Nice to have
• I would love to see cohesion between the design and colors of the two logos. I have attached a few business card designs that I like, so you can get a feel for my preferred style.

```html
<!DOCTYPE html>
<html lang="en">
<head>
<meta charset="utf-8">
<title>Quorvel Language – Business Card</title>
<link href="https://fonts.googleapis.com/css2?family=Montserrat:wght@400;600;700&family=Questrial&display=swap" rel="stylesheet">
<style>
  :root {
    --page-bg: #e9e9eb;
    --product-start: #4dbbd2;
    --product-mid: #5a8fc6;
    --product-end: #6767b6;
    --pattern-tone: rgba(70, 90, 160, 0.35);
    --white: #ffffff;
    --ink: #2b2b2f;
    --ink-soft: #5b5b60;
    --accent-blue: #3b86d3;
    --warm-1: #f7b733;
    --warm-2: #f4513f;
    --warm-3: #c53c8f;
    --cool-1: #6a5bb8;
    --cool-2: #2fc6ee;
  }
  * { margin: 0; padding: 0; box-sizing: border-box; }
  html, body {
    width: 1200px;
    height: 900px;
    overflow: hidden;
    background: var(--page-bg);
  }
  .sheet {
    position: relative;
    width: 1200px;
    height: 900px;
  }
  .card {
    position: absolute;
    left: 260px;
    width: 680px;
    height: 389px;
    overflow: hidden;
    box-shadow: 0 6px 18px rgba(0, 0, 0, 0.12);
  }

  /* Product side */
  .card--product {
    top: 41px;
    background: linear-gradient(135deg, var(--product-start) 0%, var(--product-mid) 55%, var(--product-end) 100%);
    color: var(--white);
  }
  .product-pattern {
    position: absolute;
    inset: 0;
    background: linear-gradient(160deg, rgba(255,255,255,0.06), var(--pattern-tone));
  }
  .product-mark {
    position: absolute;
    left: 392px;
    top: 178px;
    display: flex;
    align-items: center;
    gap: 14px;
  }
  .product-mark__dot {
    width: 46px;
    height: 46px;
    border-radius: 50%;
    background: var(--white);
  }
  .product-mark__name {
    font-family: "Montserrat", sans-serif;
    font-weight: 600;
    font-size: 38px;
    letter-spacing: 0.5px;
  }
  .product-rule {
    position: absolute;
    height: 1px;
    background: rgba(255, 255, 255, 0.85);
  }
  .product-rule--left { left: 30px; top: 258px; width: 220px; }
  .product-rule--right { left: 420px; top: 338px; width: 230px; }
  .product-tagline {
    position: absolute;
    left: 0;
    right: 0;
    top: 268px;
    text-align: center;
    font-family: "Questrial", sans-serif;
    font-size: 21px;
    letter-spacing: 0.4px;
  }
  .product-url {
    position: absolute;
    left: 0;
    right: 0;
    top: 300px;
    text-align: center;
    font-family: "Questrial", sans-serif;
    font-size: 19px;
    letter-spacing: 0.4px;
  }

  /* Contact side */
  .card--contact {
    top: 470px;
    background: var(--white);
  }
  .company-mark {
    position: absolute;
    left: 40px;
    top: 42px;
    display: flex;
    align-items: center;
    gap: 16px;
  }
  .company-mark__dot {
    width: 58px;
    height: 58px;
    border-radius: 50%;
    background: linear-gradient(180deg, var(--warm-2), var(--warm-3) 50%, var(--cool-1));
  }
  .company-mark__name {
    font-family: "Questrial", sans-serif;
    font-size: 36px;
    letter-spacing: 6px;
    color: var(--ink);
  }
  .company-mark__sub {
    position: absolute;
    left: 115px;
    top: 92px;
    font-family: "Questrial", sans-serif;
    font-size: 16px;
    letter-spacing: 7px;
    color: var(--ink-soft);
  }
  .holder-name {
    position: absolute;
    left: 44px;
    top: 180px;
    font-family: "Montserrat", sans-serif;
    font-weight: 600;
    font-size: 27px;
    color: var(--ink-soft);
  }
  .holder-title {
    position: absolute;
    left: 44px;
    top: 218px;
    font-family: "Questrial", sans-serif;
    font-size: 19px;
    color: var(--accent-blue);
  }
  .contact-list {
    position: absolute;
    left: 40px;
    top: 278px;
    list-style: none;
  }
  .contact-list__item {
    display: flex;
    align-items: center;
    gap: 14px;
    height: 38px;
    font-family: "Questrial", sans-serif;
    font-size: 19px;
    color: var(--ink-soft);
  }
  .contact-icon {
    width: 24px;
    height: 24px;
    flex: none;
  }
  .brand-field {
    position: absolute;
    left: 470px;
    top: 28px;
    width: 180px;
    height: 345px;
    border-radius: 90px;
    background: linear-gradient(180deg, var(--warm-1) 0%, var(--warm-2) 28%, var(--warm-3) 50%, var(--cool-1) 72%, var(--cool-2) 100%);
  }
</style>
</head>
<body>
<main class="sheet">

  <section class="card card--product" aria-label="Product side">
    <div class="product-pattern" role="img" aria-label="Repeating pattern of product symbols"></div>
    <div class="product-mark">
      <span class="product-mark__dot"></span>
      <span class="product-mark__name">Lumidrasc</span>
    </div>
    <span class="product-rule product-rule--left"></span>
    <p class="product-tagline">Culturally Immersive Language Learning Games</p>
    <p class="product-url">www.lumidrasc.example</p>
    <span class="product-rule product-rule--right"></span>
  </section>

  <section class="card card--contact" aria-label="Contact side">
    <div class="company-mark">
      <span class="company-mark__dot"></span>
      <span class="company-mark__name">QUORVEL</span>
    </div>
    <span class="company-mark__sub">LANGUAGE</span>

    <h1 class="holder-name">Perry Hollins</h1>
    <p class="holder-title">Founder | CEO</p>

    <ul class="contact-list">
      <li class="contact-list__item">
        <svg class="contact-icon" viewBox="0 0 24 24" aria-hidden="true">
          <defs>
            <linearGradient id="iconGradPhone" x1="0" y1="0" x2="0" y2="1">
              <stop offset="0" stop-color="#c53c8f"/>
              <stop offset="1" stop-color="#6a5bb8"/>
            </linearGradient>
          </defs>
          <circle cx="12" cy="12" r="12" fill="url(#iconGradPhone)"/>
          <path d="M8.6 6.5l1.7 2.2-1 1.2c.7 1.6 2 2.9 3.6 3.7l1.2-1 2.2 1.6-.9 2c-4.4-.3-7.7-3.6-8-8z" fill="#fff"/>
        </svg>
        <span>(555)-014-2736</span>
      </li>
      <li class="contact-list__item">
        <svg class="contact-icon" viewBox="0 0 24 24" aria-hidden="true">
          <defs>
            <linearGradient id="iconGradMail" x1="0" y1="0" x2="0" y2="1">
              <stop offset="0" stop-color="#c53c8f"/>
              <stop offset="1" stop-color="#6a5bb8"/>
            </linearGradient>
          </defs>
          <circle cx="12" cy="12" r="12" fill="url(#iconGradMail)"/>
          <rect x="6.5" y="8" width="11" height="8" rx="1" fill="none" stroke="#fff" stroke-width="1.4"/>
          <path d="M6.8 8.5L12 12.6l5.2-4.1" fill="none" stroke="#fff" stroke-width="1.4"/>
        </svg>
        <span>phollins@mailtrove.example</span>
      </li>
    </ul>

    <div class="brand-field" role="img" aria-label="Large decorative brand numeral in warm-to-cool gradient"></div>
  </section>

</main>
</body>
</html>
```